Business Card Design for a Private Label Pet Company

We need a business card design for our family-owned company, Hollow Creek Pet Works (www.hollowcreekpetworks.com), out of St. Louis, MO. We provide turnkey private label solutions for retailers, Marketvale sellers and other brands who want to provide high quality, natural, Made in the USA pet products to their customers. Our customer are worldwide and range from the US to the UK to Vietnam and beyond. We offer private label for dozens of pet products including grooming products (shampoos, conditioners, colognes, ear and eye washes, mouthwash, etc.), all meat treats, supplements, and specialty products (pet stain and odor cleaner, anti-chew spray, etc.). We would like to see designs that use the colors, fonts and logos (see variations) within our brand guidelines and fit with the look and feel from our website.

Target Market(s)

Pet Store Owners, Marketvale Sellers, Pet Brand Marketers

Industry/Entity Type

Pet

Contact Information for Business Card

Tom Willoughby
CEO
Hollow Creek Pet Works
5817 Brookhaven Commerce Lane
St. Louis, MO 63521
office: 314.555.0182
mobile: 770.555.0139
email: tom@hollowcreekpetworks.com

Colors

Designer to choose colors to be used in the design.

Requirements
Must have
• Need to follow the brand guidelines attached for colors, fonts and logos
• Need to use the logos attached (or a variation) with our without the tagline
• Name, title, phone (office and mobil), email, address on the business card
• Clean professional look and feel that says: high quality natural pet products, high quality service, made in the USA
Nice to have
• Made in the USA is a big positive in our industry and we are very proud of it. There is an attached icon from our website. The designer can get creative here as they wish.
• I do like using color for pop. Just don't like lots of bright, loud colors.
Should not have
• lots of bright, loud colors
• overwhelming to the reader
• crowded

```html
<!DOCTYPE html>
<html lang="en">
<head>
<meta charset="utf-8">
<title>Hollow Creek Pet Works – Business Card</title>
<link rel="stylesheet" href="https://fonts.googleapis.com/css2?family=Raleway:wght@300;400;500;600;700&family=Open+Sans:wght@400&display=swap">
<style>
  :root {
    --bg: #8e8e8e;
    --panel-light: #d8d9dc;
    --panel-dark: #444444;
    --accent-green: #88a55a;
    --slate: #4a625d;
    --taupe: #a9a18c;
    --rule: #a9a79c;
  }
  * { box-sizing: border-box; margin: 0; padding: 0; }
  html, body { width: 1200px; height: 1200px; overflow: hidden; }
  body {
    background: var(--bg);
    font-family: "Raleway", sans-serif;
    position: relative;
  }
  .card {
    position: absolute;
    left: 236px;
    width: 728px;
    height: 437px;
    border-radius: 16px;
    overflow: hidden;
    background: var(--panel-dark);
    box-shadow: 0 2px 8px rgba(0,0,0,0.25);
  }
  .card--front { top: 121px; }
  .card--back { top: 642px; }
  .card__green {
    position: absolute; left: 0; top: 0; width: 100%;
    background: var(--accent-green);
  }
  .card__light {
    position: absolute; left: 0; top: 0; width: 100%;
    background: var(--panel-light);
    border-bottom-right-radius: 30px;
  }
  .card--front .card__green { height: 340px; }
  .card--front .card__light { height: 329px; }
  .card--back .card__green { height: 221px; }
  .card--back .card__light { height: 210px; }

  .brand-name {
    position: absolute; left: 0; right: 0; top: 98px;
    text-align: center;
    font-weight: 700; font-size: 50px; letter-spacing: 0.5px;
    color: var(--slate);
    text-transform: uppercase;
  }
  .brand-rule {
    position: absolute; left: 136px; right: 136px; top: 190px;
    border-top: 1px solid var(--rule);
    border-bottom: 1px solid var(--rule);
    height: 4px;
  }
  .tagline {
    position: absolute; left: 0; right: 0; top: 219px;
    text-align: center;
    font-weight: 500; font-size: 23px; letter-spacing: 0.6px;
    color: var(--slate);
  }
  .website {
    position: absolute; left: 0; right: 0; top: 363px;
    text-align: center;
    font-family: "Open Sans", sans-serif;
    font-size: 24px; color: var(--taupe);
  }
  .dot {
    position: absolute;
    width: 34px; height: 34px; border-radius: 50%;
    background: var(--taupe);
  }
  .card--front .dot { left: 50px; top: 365px; }
  .card--back .dot { left: 668px; top: 373px; }

  .person {
    position: absolute; left: 0; right: 0; top: 66px;
    text-align: center;
  }
  .person__name {
    display: inline-block;
    font-weight: 500; font-size: 44px; color: var(--slate);
    line-height: 1.1;
    padding-bottom: 2px;
    border-bottom: 4px double var(--slate);
  }
  .person__title {
    margin-top: 6px;
    font-weight: 400; font-size: 29px; color: var(--slate);
  }
  .contact {
    position: absolute; left: 0; right: 0; top: 246px;
    text-align: center; color: var(--taupe);
  }
  .contact__company { font-weight: 600; font-size: 35px; line-height: 1.15; margin-bottom: 4px; }
  .contact__line { font-weight: 300; font-size: 21px; line-height: 26px; }
  .contact__line .gap { display: inline-block; width: 24px; }
  .contact__email { font-weight: 600; font-size: 21px; margin-top: 10px; }
</style>
</head>
<body>
  <section class="card card--front" aria-label="Card front">
    <div class="card__green"></div>
    <div class="card__light"></div>
    <div class="brand-name">Hollow Creek Pet Works</div>
    <div class="brand-rule"></div>
    <p class="tagline">TURNKEY PRIVATE LABEL PARTNER</p>
    <span class="dot"></span>
    <p class="website">www.hollowcreekpetworks.com</p>
  </section>

  <section class="card card--back" aria-label="Card back">
    <div class="card__green"></div>
    <div class="card__light"></div>
    <div class="person">
      <h1 class="person__name">Tom Willoughby</h1>
      <p class="person__title">CEO</p>
    </div>
    <div class="contact">
      <p class="contact__company">Hollow Creek Pet Works™</p>
      <p class="contact__line">5817 Brookhaven Commerce Lane</p>
      <p class="contact__line">St. Louis, MO 63521</p>
      <p class="contact__line">office: 314.555.0182<span class="gap"></span>mobile: 770.555.0139</p>
      <p class="contact__email">email: tom@hollowcreekpetworks.com</p>
    </div>
    <span class="dot"></span>
  </section>
</body>
</html>
```